Box design for Jade Roller and gua sha set

Hello I am looking to have a box designed for a Jade Roller and gua sha set. The dimensions have already been Determined. There will be 3 sides with design, 2 sides on the outside with design and 1 on the inside of the box for instructions.

I have attached an Ai file that has the exact dimensions of the box.
I have also attached a few pictures of my product, please find the best way to use them on the box design along with my logos (which I will also attach).

The title of the product is "Jade Roller & Gua Sha Set".

The brand for this product is Willowmere Goods (please use the logo provided)

I have attached a second logo that says "Brinvale, Willowmere Goods...Willowmere Goods is a part of the Brinvale Group" Please put this somewhere on the back side of the packaging (preferably at the bottom right corner, small)
Also on the back side please neatly place these features:
SUPERIOR QUALITY: Made from real Jade Stone and developed with high quality materials which result in smooth, noise free rolling
BLOOD CIRCULATION: The Jade Roller has two sides, the bigger side for the general facial area and the smaller side for more accurate massaging around the eyes
ROLL AWAY AGE AND PUFFY DARK EYES: This roller will reduce the dark circles and puffiness around your eyes by circulating blood flow which allows more blood cells to get to places which is difficult without rolling. It will also help reduce the appearance of wrinkles on the forehead with the same method.
GUA SHA TOOL: Included is a Gua Sha tool which is very effective for eye massaging, facial lifting and body scraping
VELVET TRAVEL BAG: Included is also a small carrying bag for the roller and gua sha that tightens

For the inside of the box please insert the instructions photo I have provided. I want to be able to edit the words in this after so please make sure I can do that in adobe.

```html
<!DOCTYPE html>
<html lang="en">
<head>
<meta charset="utf-8">
<title>Jade Roller &amp; Gua Sha Set — Box Dieline</title>
<link href="https://fonts.googleapis.com/css2?family=Cinzel:wght@500;600&family=Lato:wght@400;700&family=Roboto+Condensed:wght@400;700&family=Noto+Serif+SC:wght@400&display=swap" rel="stylesheet">
<style>
  :root{
    --jade:#0b8a45;
    --jade-deep:#17733d;
    --jade-soft:#d7efe0;
    --gold:#f7c20c;
    --lime:#8fb33a;
    --ink:#333;
    --grey-band:#ececec;
    --glue:#f0b0ad;
    --line:#8a8a8a;
    --paper:#fff;
  }
  *{box-sizing:border-box;margin:0;padding:0}
  html,body{width:800px;height:1200px;overflow:hidden;background:var(--paper)}
  .canvas{position:relative;width:800px;height:1200px}
  .abs{position:absolute}

  .dieline-outline{position:absolute;left:0;top:0}

  /* title lockup */
  .title-lockup{position:absolute;border:1.6px solid var(--jade-deep);border-right:none;
    font-family:"Cinzel",serif;color:var(--jade-deep);line-height:1;white-space:nowrap}
  .title-lockup .title{display:block;font-weight:600;letter-spacing:.01em}
  .title-lockup .title .cap{font-size:1.25em}
  .title-lockup .subtitle{position:absolute;right:-2px;bottom:0;transform:translateY(55%);background:var(--paper);
    color:var(--lime);padding:0 2px 0 3px;font-weight:500;line-height:1}
  .title-lockup::after{content:"";position:absolute;right:0;top:0;width:1.6px;height:62%;background:var(--jade-deep)}

  /* back panel */
  .back-panel{left:49px;top:304px;width:346px;height:234px;border:1px solid #ddd;background:var(--paper)}
  .back-inner{position:absolute;inset:0;transform:rotate(180deg);padding:14px 16px 10px 14px}
  .feature{position:relative;padding-left:9px;margin-bottom:8px;font-family:"Roboto Condensed",sans-serif;
    font-size:7.2px;line-height:1.45;color:var(--ink)}
  .feature::before{content:"";position:absolute;left:0;top:3px;width:3.4px;height:3.4px;border-radius:50%;background:var(--gold)}
  .feature b{color:var(--jade);font-weight:700}
  .group-mark{position:absolute;right:16px;bottom:12px;text-align:left;font-family:"Roboto Condensed",sans-serif}
  .group-mark .group-name{display:flex;align-items:center;gap:3px;font-size:5px;color:var(--ink)}
  .group-mark .group-name i{width:4px;height:4px;border-radius:50%;background:var(--jade);display:block}
  .group-mark .big{font-weight:700;font-size:10px;letter-spacing:.06em;color:#111}

  .band{position:absolute;left:49px;width:346px}
  .band-yellow{top:542px;height:50px;background:var(--gold)}
  .band-green{top:835px;height:50px;background:var(--jade)}

  /* front panel */
  .front-panel{left:49px;top:597px;width:346px;height:233px;border:1px solid #ddd;overflow:hidden;
    background:linear-gradient(45deg,var(--jade-soft) 0%,#eef8f2 18%,var(--paper) 40%)}
  .product-photo{position:absolute;left:150px;top:70px;width:196px;height:163px;
    background:linear-gradient(135deg,#e4f3e8 0%,#b9d9a8 50%,#d8ecd0 100%)}
  .brand-lockup{position:absolute;display:flex;align-items:center;gap:4px;font-family:"Lato",sans-serif;
    font-weight:700;color:#222;text-transform:uppercase;letter-spacing:.04em}
  .brand-lockup i{display:block;border-radius:50%;background:#c8202f}

  /* instructions panel */
  .glue-head{left:437px;top:508px;width:340px;height:50px;background:var(--grey-band);border:1px solid #d5d5d5}
  .instructions{left:437px;top:562px;width:340px;height:214px;border:1px solid #ccc;
    background:linear-gradient(135deg,var(--paper) 40%,#e4f4ea 100%);
    display:grid;grid-template-columns:1fr 1fr 1fr;gap:10px;padding:9px 12px}
  .step h4{font-family:"Lato",sans-serif;font-size:4.6px;font-weight:700;color:#222;margin-bottom:1.5px}
  .step p{font-family:"Lato",sans-serif;font-size:4.2px;line-height:1.45;color:#444;margin-bottom:5px}
  .col-first .step h4,.col-first .step p{color:var(--jade)}
  .col-first .step:last-of-type h4,.col-first .step:last-of-type p{color:#333}
  .face-art{height:44px;margin:3px 0 7px;border-radius:4px;
    background:linear-gradient(135deg,rgba(11,138,69,.08),rgba(247,194,12,.18))}
  .glue-area{left:437px;top:780px;width:340px;height:39px;background:var(--glue);
    display:flex;align-items:center;justify-content:center;font-family:"Noto Serif SC",serif;font-size:16px;color:#333}
</style>
</head>
<body>
<div class="canvas">

  <svg class="dieline-outline" width="800" height="1200" viewBox="0 0 800 1200" aria-hidden="true">
    <polygon points="58,277 387,277 423,313 423,884 387,920 58,920 22,884 22,313"
      fill="none" stroke="var(--line)" stroke-width="0.8"/>
  </svg>

  <!-- back panel (printed upside down on the dieline) -->
  <section class="abs back-panel">
    <div class="back-inner">
      <p class="feature"><b>SUPERIOR QUALITY:</b> Made from real Jade Stone and developed with high quality materials which result in smooth, noise free rolling.</p>
      <p class="feature"><b>BLOOD CIRCULATION:</b> The Jade Roller has two sides, the bigger side for the general facial area and the smaller side for more accurate massaging around the eyes.</p>
      <p class="feature"><b>ROLL AWAY AGE AND PUFFY DARK EYES:</b> This roller will reduce the dark circles and puffiness around your eyes by circulating blood flow which allows more blood cells to get to places which is difficult without rolling. It will also help reduce the appearance of wrinkles on the forehead with the same method.</p>
      <p class="feature"><b>GUA SHA TOOL:</b> Included is a Gua Sha tool which is very effective for eye massaging, facial lifting and body scraping.</p>
      <p class="feature"><b>VELVET TRAVEL BAG:</b> Included is also a small carrying bag for the roller and gua sha that tightens.</p>
      <div class="group-mark">
        <div class="group-name"><i></i>Willowmere Goods</div>
        <div class="big">BRINVALE</div>
      </div>
    </div>
  </section>

  <div class="band band-yellow">
    <div class="title-lockup" style="left:120px;top:13px;font-size:13px;padding:3px 6px 4px 6px;transform:rotate(180deg)">
      <span class="title"><span class="cap">J</span>ADE <span class="cap">R</span>OLLER</span>
      <span class="subtitle" style="font-size:4.5px;background:var(--gold)">&amp; GUA SHA SET</span>
    </div>
  </div>

  <!-- front panel -->
  <section class="abs front-panel">
    <div class="product-photo" role="img" aria-label="Product photo: jade face roller with gold handle and a pale jade gua sha stone, with decorative arcs"></div>
    <div class="title-lockup" style="left:30px;top:21px;font-size:26px;padding:4px 8px 7px 8px">
      <span class="title"><span class="cap">J</span>ADE <span class="cap">R</span>OLLER</span>
      <span class="subtitle" style="font-size:9px">&amp; GUA SHA SET</span>
    </div>
    <div class="brand-lockup" style="left:31px;top:198px;font-size:8.5px"><i style="width:11px;height:11px"></i>Willowmere Goods</div>
  </section>

  <div class="band band-green">
    <div class="title-lockup" style="left:120px;top:13px;font-size:13px;padding:3px 6px 4px 6px;color:#fff;border-color:var(--gold)">
      <span class="title"><span class="cap">J</span>ADE <span class="cap">R</span>OLLER</span>
      <span class="subtitle" style="font-size:4.5px;background:var(--jade);color:var(--gold)">&amp; GUA SHA SET</span>
    </div>
  </div>

  <!-- inside flap: instructions -->
  <div class="abs glue-head">
    <div class="title-lockup" style="left:120px;top:14px;font-size:12px;padding:3px 6px 4px 6px">
      <span class="title"><span class="cap">J</span>ADE <span class="cap">R</span>OLLER</span>
      <span class="subtitle" style="font-size:4.2px;background:var(--grey-band)">&amp; GUA SHA SET</span>
    </div>
  </div>

  <section class="abs instructions">
    <div class="col-first">
      <div class="step"><h4>Directions:</h4><p>Glide the roller over clean skin two to three times daily for five to ten minutes. Use light pressure only. Apply after serum or moisturiser to help products absorb deeper into the skin.</p></div>
      <div class="step"><h4>Cleaning:</h4><p>Wipe the stone with a soft damp cloth, then dry it fully before storing. Do not soak in hot water or use harsh cleaners.</p></div>
      <div class="step"><h4>Forehead</h4><p>From the centre of the forehead, roll outward to the hairline. Repeat three to six times.</p></div>
      <div class="face-art" role="img" aria-label="Line drawing showing roller strokes across the forehead"></div>
    </div>
    <div>
      <div class="step"><h4>Eyes</h4><p>Use the small roller under the eyes, rolling from the inner corner out to the ear.</p></div>
      <div class="face-art" role="img" aria-label="Line drawing showing roller strokes under the eyes"></div>
      <div class="step"><h4>For sinus pain and pressure</h4><p>Warm a washcloth and press it over the face for ten seconds. Then roll from the centre of the face down to below the cheekbones.</p></div>
      <div class="face-art" role="img" aria-label="Line drawing showing roller strokes over the cheekbones"></div>
    </div>
    <div>
      <div class="step"><h4>Nose, lips and chin</h4><p>Roll from the nose out to the ear, then along the upper lip and chin. Repeat on the other side.</p></div>
      <div class="face-art" role="img" aria-label="Line drawing showing roller strokes around the nose, lips and chin"></div>
      <div class="step"><h4>Jawline and neck</h4><p>Start at the chin and roll outward and up along the jaw, then sweep down the neck toward the collarbone.</p></div>
      <div class="face-art" role="img" aria-label="Line drawing showing roller strokes along the jawline and neck"></div>
    </div>
  </section>

  <div class="abs glue-area">沾胶位置</div>

</div>
</body>
</html>
```